Policy Manual in Education

I need the attached document to be put in a publishable format, with graphics a professional layout, and something that looks more like a professional report, etc. Use color samples from http://www.brwt-qx.com/ and www.kv7lo.com, my company is Kv7lo, we were hired to write the report and we also built the BRWT resource center http://www.brwt-qx.com/ .

Target Market(s)

Education

Requirements
Must have
• Look and feel around NM. http://www.brwt-qx.com/ and www.kv7lo.com

```html
<!DOCTYPE html>
<html lang="en">
<head>
<meta charset="utf-8">
<title>Policy Manual in Education — First steps and Building your student population</title>
<link rel="stylesheet" href="https://fonts.googleapis.com/css2?family=Arimo:ital,wght@0,400;0,700;1,400&display=swap">
<style>
  :root {
    --desk: #b8bcc2;
    --desk-dark: #8f949b;
    --paper: #ffffff;
    --ink: #111111;
    --rule: #a9b8c9;
    --brand: #4f7fb8;
    --footer-ink: #7f91a8;
    --node-light: #6f9bd2;
    --node-dark: #3b6aa6;
    --ring: #d5dde8;
    --ring-edge: #98a9c0;
  }
  * { box-sizing: border-box; margin: 0; padding: 0; }
  html, body { width: 1200px; height: 718px; overflow: hidden; }
  body {
    position: relative;
    background: linear-gradient(90deg, var(--desk-dark) 0, var(--desk) 60px, var(--desk) 100%);
    font-family: "Arimo", Arial, sans-serif;
    color: var(--ink);
  }
  .page {
    position: absolute;
    top: 5px;
    height: 709px;
    background: var(--paper);
    box-shadow: 0 0 3px rgba(0,0,0,.35);
  }
  .page--left { left: 64px; width: 560px; }
  .page--right { left: 636px; width: 562px; }

  .page__header {
    position: absolute; left: 5px; right: 5px; top: 0; height: 44px;
    border-bottom: 1px solid var(--rule);
    display: flex; align-items: center; justify-content: center;
  }
  .brand-name {
    font-family: "Arimo", Arial, sans-serif;
    font-weight: 700; font-size: 22px; letter-spacing: 1px;
    color: var(--brand);
  }

  .page__body {
    position: absolute; left: 66px; width: 428px; top: 70px;
    font-size: 11.2px; line-height: 12.4px; text-align: justify;
  }
  .page__title { font-size: 13px; font-weight: 700; margin-bottom: 26px; text-align: left; }
  .page--right .page__title { margin-bottom: 14px; }
  .intro { text-indent: 32px; margin-bottom: 6px; }

  .diagram-space { float: right; width: 180px; margin-left: 8px; }
  .page--left .diagram-space { height: 236px; margin-top: -38px; }
  .page--right .diagram-space { height: 232px; margin-top: -26px; }

  .points { list-style: none; }
  .points > li { position: relative; padding-left: 32px; margin-bottom: 1px; }
  .points > li::before { content: "\2666"; position: absolute; left: 16px; font-size: 10px; }
  .subpoints { list-style: none; }
  .subpoints > li { position: relative; padding-left: 34px; }
  .subpoints > li::before { content: "\27A2"; position: absolute; left: 19px; font-size: 10px; }
  .points--gap { margin-top: 13px; }
  .closing { text-indent: 32px; margin-top: 15px; }

  .diagram { position: absolute; }
  .page--left .diagram { left: 314px; top: 90px; }
  .page--right .diagram { left: 326px; top: 90px; }
  .node-label { font-family: "Arimo", Arial, sans-serif; font-size: 6px; fill: #fff; text-anchor: middle; }
  .hub-label { font-family: "Arimo", Arial, sans-serif; fill: #fff; text-anchor: middle; }

  .page__footer {
    position: absolute; left: 44px; width: 474px; top: 664px;
    border-top: 1px solid var(--rule);
    font-size: 11px; color: var(--footer-ink);
  }
  .page--right .page__footer { left: 43px; }
  .page-number { position: absolute; left: 236px; top: 5px; }
  .running-title { position: absolute; right: 8px; top: 2px; font-style: italic; font-size: 11.5px; }
</style>
</head>
<body>

<article class="page page--left">
  <header class="page__header"><span class="brand-name">QLDEP</span></header>

  <svg class="diagram" width="204" height="204" viewBox="0 0 204 204" aria-hidden="true">
    <defs>
      <radialGradient id="node-fill-a" cx="50%" cy="35%" r="65%">
        <stop offset="0" stop-color="var(--node-light)"/><stop offset="1" stop-color="var(--node-dark)"/>
      </radialGradient>
    </defs>
    <circle cx="101" cy="102" r="91" fill="none" stroke="var(--ring-edge)" stroke-width="9"/>
    <circle cx="101" cy="102" r="91" fill="none" stroke="var(--ring)" stroke-width="7"/>
    <circle cx="101" cy="102" r="36" fill="url(#node-fill-a)" stroke="#fff" stroke-width="2"/>
    <text class="hub-label" x="101" y="98" font-size="16">First</text>
    <text class="hub-label" x="101" y="117" font-size="16">Steps</text>
    <circle cx="101" cy="26" r="29" fill="url(#node-fill-a)" stroke="#fff" stroke-width="2"/>
    <text class="node-label" x="101" y="12">Funding is</text>
    <text class="node-label" x="101" y="19">adequate for</text>
    <text class="node-label" x="101" y="26">current</text>
    <text class="node-label" x="101" y="33">development</text>
    <text class="node-label" x="101" y="40">and sustainability</text>
    <circle cx="38" cy="170" r="29" fill="url(#node-fill-a)" stroke="#fff" stroke-width="2"/>
    <text class="node-label" x="38" y="159">Your</text>
    <text class="node-label" x="38" y="166">outcomes</text>
    <text class="node-label" x="38" y="173">are clear</text>
    <text class="node-label" x="38" y="180">and</text>
    <text class="node-label" x="38" y="187">measurable</text>
    <circle cx="165" cy="170" r="29" fill="url(#node-fill-a)" stroke="#fff" stroke-width="2"/>
    <text class="node-label" x="165" y="156">Key issues</text>
    <text class="node-label" x="165" y="163">are</text>
    <text class="node-label" x="165" y="170">addressed</text>
    <text class="node-label" x="165" y="177">in your</text>
    <text class="node-label" x="165" y="184">policies</text>
  </svg>

  <section class="page__body">
    <h2 class="page__title">First steps</h2>
    <div class="diagram-space"></div>
    <p class="intro">The following three first steps will begin design of your BRWT, establishing a foundation for development.</p>
    <ul class="points">
      <li>Assure you have committed budget funds to increase sustainability and scalability, and understand fundraising is regular and ongoing.
        <ul class="subpoints">
          <li>BRWTs can be expensive with money needed to pay tuition, books, and fees for the college credit-bearing courses students take.</li>
          <li>You may need to consider student transportation fees when the BRWT is located on a college campus—both for students and parents to remain involved.</li>
          <li>You will also need funds to support the comprehensive student support systems so crucial to program success.</li>
          <li>Relationships with community organizations, business and industry leaders, and others are integral to keeping funding pipelines. Also of value are public and private grant opportunities.</li>
          <li>Students attending schools in need of improvement, high-priority schools, or students from lower SES could qualify for ESSA funding, discussed earlier in this manual.</li>
        </ul>
      </li>
    </ul>
    <ul class="points points--gap">
      <li>When developing your policies and procedures, make sure you address the most important issues to your design.</li>
      <li>Establish clearly written goals, with measurable outcomes for students and the program.</li>
    </ul>
  </section>

  <footer class="page__footer">
    <span class="page-number">39</span>
    <span class="running-title">Policy Manual in Education</span>
  </footer>
</article>

<article class="page page--right">
  <header class="page__header"><span class="brand-name">QLDEP</span></header>

  <svg class="diagram" width="204" height="204" viewBox="0 0 204 204" aria-hidden="true">
    <defs>
      <radialGradient id="node-fill-b" cx="50%" cy="35%" r="65%">
        <stop offset="0" stop-color="var(--node-light)"/><stop offset="1" stop-color="var(--node-dark)"/>
      </radialGradient>
    </defs>
    <circle cx="101" cy="103" r="91" fill="none" stroke="var(--ring-edge)" stroke-width="9"/>
    <circle cx="101" cy="103" r="91" fill="none" stroke="var(--ring)" stroke-width="7"/>
    <circle cx="101" cy="103" r="37" fill="url(#node-fill-b)" stroke="#fff" stroke-width="2"/>
    <text class="hub-label" x="101" y="100" font-size="10.5">Student</text>
    <text class="hub-label" x="101" y="114" font-size="10.5">Population</text>
    <circle cx="101" cy="27" r="29" fill="url(#node-fill-b)" stroke="#fff" stroke-width="2"/>
    <text class="node-label" x="101" y="13">Student</text>
    <text class="node-label" x="101" y="20">composition</text>
    <text class="node-label" x="101" y="27">mirrors that</text>
    <text class="node-label" x="101" y="34">of your</text>
    <text class="node-label" x="101" y="41">district</text>
    <circle cx="101" cy="179" r="29" fill="url(#node-fill-b)" stroke="#fff" stroke-width="2"/>
    <text class="node-label" x="101" y="165">Recruitment</text>
    <text class="node-label" x="101" y="172">and marketing</text>
    <text class="node-label" x="101" y="179">strategies to</text>
    <text class="node-label" x="101" y="186">support</text>
    <text class="node-label" x="101" y="193">diversity</text>
  </svg>

  <section class="page__body">
    <h2 class="page__title">Building your student population</h2>
    <div class="diagram-space"></div>
    <p class="intro">Your student population must be reflective of the basic vision of the BRWT model.</p>
    <ul class="points">
      <li>Make sure the demographic composition of your BRWT population mirrors that of the district in which it operates.
        <ul class="subpoints">
          <li>Selection solely by lottery is not sufficient to carry out this vision. Schools must take into account how to define “low income,” which groups of low-income and underserved populations will be targeted, and in what ratios will they be recruited to reflect the district composition. Some examples are to determine whether your program aim includes ESL students, recent immigrants, students with poor attendance, students struggling with academics at their current grade level, and others.</li>
          <li>How many students are needed to mirror the district’s demographics in corresponding subgroups?</li>
        </ul>
      </li>
      <li>A detailed recruitment and marketing strategy will help establish the application and acceptance processes in BRWTs.
        <ul class="subpoints">
          <li>You will need to establish a flow of responsibility for the recruitment and marketing process. This may include presentations by BRWT leaders, postsecondary partners, and business partners as well.</li>
          <li>Consider what you will require for application criteria—e.g., teacher recommendation, test scores, grades, and/or student and parent commitment.</li>
          <li>It is important to use measures that ensure students with low cultural capital and/or low family support are not further disenfranchised from educational and career opportunities.</li>
        </ul>
      </li>
    </ul>
    <p class="closing">Parents and students alike must be well-informed on the BRWTs. This information should be available to them during the recruitment and application timeline each year, and from individual meetings with school counselors throughout the year, although particularly during the application period.</p>
  </section>

  <footer class="page__footer">
    <span class="page-number">40</span>
    <span class="running-title">Policy Manual in Education</span>
  </footer>
</article>

</body>
</html>
```